Flyer for Institute Party

This event has changed to the following - March 24th, 2017 from 4-6pm in the Halvern Medical Education Center Atrium (You can get to the Atrium from the Drentby elevators by getting off on the 5th floor or from the Crestmoor Pavilion elevators by getting off on the 5th floor). I have attached the logo of the Institute as well to add to the flyer. Also, the Lumaris Institute just became and Institute in January 2017, so it would be nice to note that as part of the celebration in the flyer someplace. We have a lot to celebrate! I am looking for a fun flyer to for an Institute party. We would like to celebrate becoming an Institute and the labs within the Institute at the party.

```html
<!DOCTYPE html>
<html lang="en">
<head>
<meta charset="utf-8">
<title>Celebrate – Corvale Lumaris Institute</title>
<link rel="stylesheet" href="https://fonts.googleapis.com/css2?family=Playball&family=PT+Sans:wght@400;700&family=Montserrat:wght@600&display=swap">
<style>
  :root {
    --night: #2a1a78;
    --night-deep: #1c0f5c;
    --ribbon-red: #e0452e;
    --ribbon-green: #4fb52a;
    --ribbon-blue: #2d6fd6;
    --ribbon-orange: #f07a1a;
    --veil: rgba(238, 232, 246, 0.62);
    --cream: #fbf8c6;
    --title-red: #c82a3c;
    --ink: #2b2b2b;
    --date-blue: #1f4e8e;
    --venue-blue: #2a6cb4;
  }
  * { margin: 0; padding: 0; box-sizing: border-box; }
  html, body { width: 927px; height: 1200px; overflow: hidden; }
  body { position: relative; background: var(--night); font-family: "PT Sans", Arial, sans-serif; }

  .ribbon-art {
    position: absolute; inset: 0;
    background:
      radial-gradient(ellipse 60% 40% at 15% 20%, rgba(224,69,46,0.55), transparent 70%),
      radial-gradient(ellipse 50% 45% at 90% 30%, rgba(240,122,26,0.5), transparent 70%),
      radial-gradient(ellipse 55% 40% at 10% 80%, rgba(79,181,42,0.5), transparent 70%),
      radial-gradient(ellipse 60% 40% at 85% 85%, rgba(45,111,214,0.55), transparent 70%),
      radial-gradient(ellipse 40% 35% at 50% 50%, rgba(79,181,42,0.35), transparent 70%),
      linear-gradient(160deg, var(--night), var(--night-deep));
  }

  .veil {
    position: absolute; left: 140px; top: 103px; width: 648px; height: 994px;
    background: var(--veil); border-radius: 14px;
  }

  .card {
    position: absolute; left: 218px; top: 163px; width: 492px; height: 604px;
    background: var(--cream); border-radius: 12px; text-align: center;
  }
  .title {
    font-family: "Playball", cursive; font-weight: 400; color: var(--title-red);
    font-size: 104px; line-height: 1; margin-top: 30px; padding-left: 20px;
  }
  .invite {
    font-weight: 700; color: var(--ink); font-size: 25px; line-height: 30px;
    margin-top: 26px;
  }
  .when {
    font-weight: 700; color: var(--date-blue); font-size: 38px; line-height: 42px;
    margin-top: 26px;
  }
  .venue {
    font-family: "Montserrat", sans-serif; font-weight: 600; color: var(--venue-blue);
    font-size: 29px; line-height: 35px; margin-top: 22px;
  }
  .directions {
    color: var(--ink); font-size: 19px; line-height: 24px; margin-top: 4px;
  }

  .milestone {
    position: absolute; left: 140px; width: 648px; top: 778px;
    text-align: center; font-weight: 700; color: var(--ink);
    font-size: 15px; line-height: 21px;
  }

  .sponsor {
    position: absolute; left: 300px; top: 880px; width: 330px;
    display: flex; align-items: center; gap: 16px;
  }
  .sponsor-dot { width: 64px; height: 64px; border-radius: 50%; background: var(--ribbon-blue); flex: none; }
  .sponsor-name {
    font-weight: 700; color: var(--title-red); font-size: 34px; line-height: 38px;
  }
</style>
</head>
<body>
  <div class="ribbon-art" role="img" aria-label="Colourful glossy ribbons twisting like DNA helices on a deep indigo background"></div>

  <div class="veil"></div>

  <section class="card">
    <h1 class="title">Celebrate</h1>
    <p class="invite">the international day of awesomeness<br>by celebrating awesomeness in the labs<br>of the Corvale Lumaris Institute.</p>
    <p class="when">March 24, 2017<br>4:00-6:00PM</p>
    <p class="venue">The Halvern Medical<br>Education Center Atrium</p>
    <p class="directions">(You can get to the Atrium from the<br>Drentby elevators by getting off on the<br>5th floor or from the Crestmoor Pavilion<br>elevators by getting off on the 5th floor.)</p>
  </section>

  <p class="milestone">The Lumaris Institute just became<br>an Institute in January 2017.<br>We have a lot to celebrate!</p>

  <div class="sponsor">
    <span class="sponsor-dot"></span>
    <span class="sponsor-name">Corvale Lumaris Institute</span>
  </div>
</body>
</html>
```